Redesign of Website

We need an overhaul of our website. I've attached our current logo files. Please visit www.pelvorix.com for our current website for information about our company. We are looking for the same type of website (information-based only) so no need for any online store, payments, interactive stuff or anything like that...basically looking for a fresh new look! Also please make sure this design will be mobile-friendly. Thanks!

```html
<!DOCTYPE html>
<html lang="en">
<head>
<meta charset="utf-8">
<title>Pelvorix Consultants</title>
<link href="https://fonts.googleapis.com/css2?family=Arimo:wght@400;700&family=Tinos:wght@400;700&display=swap" rel="stylesheet">
<style>
:root{
  --navy:#0f2f6b;
  --navy-deep:#0a2457;
  --blue:#1d5fb4;
  --blue-mid:#2f72c0;
  --blue-soft:#5b8fce;
  --ink:#222;
  --grey:#666;
  --line:#dcdcdc;
  --white:#fff;
}
*{margin:0;padding:0;box-sizing:border-box}
html,body{width:1200px;height:3191px;overflow:hidden;background:var(--white);font-family:"Arimo",Arial,sans-serif;color:var(--ink)}
.page{position:relative;width:1200px;height:3191px}
.site-header{position:absolute;top:0;left:0;width:1200px;height:96px;display:flex;align-items:center;justify-content:space-between;padding:0 80px 0 90px}
.brand{display:flex;align-items:center;gap:12px;font-weight:700;font-size:34px;color:var(--navy);letter-spacing:1px}
.brand-mark{width:18px;height:18px;background:var(--navy)}
.nav{display:flex;gap:44px;font-family:"Tinos",serif;font-size:19px;color:#333;letter-spacing:.5px}
.hero{position:absolute;top:96px;left:0;width:1200px;height:494px;background:linear-gradient(180deg,#5d7fae 0%,#3e67a3 45%,#2c5594 100%);color:var(--white)}
.hero-content{position:absolute;left:330px;top:178px;width:560px}
.hero h1{font-size:34px;font-weight:700;margin-bottom:20px}
.hero p{font-size:15.5px;line-height:1.65}
.btn-light{display:inline-block;margin-top:22px;background:var(--blue);color:var(--white);font-size:14px;font-weight:700;padding:11px 22px;letter-spacing:.5px}
.features{position:absolute;top:672px;left:70px;width:1053px;height:220px;display:flex}
.feature{flex:1;display:flex;flex-direction:column;align-items:center;text-align:center;color:var(--white);padding-top:32px}
.feature:nth-child(1){background:#2c6cb4}
.feature:nth-child(2){background:#174b94;margin-top:-12px;padding-top:44px}
.feature:nth-child(3){background:#3a7dc4}
.feature h3{font-size:21px;margin:16px 0 10px}
.feature p{font-size:15px;line-height:1.35}
.diamond{width:52px;height:52px;border:2px solid var(--white);transform:rotate(45deg);display:flex;align-items:center;justify-content:center}
.diamond svg{transform:rotate(-45deg)}
.about{position:absolute;top:976px;left:0;width:1200px;height:380px;background:var(--navy)}
.about-photo{position:absolute;right:0;top:0;width:620px;height:380px;background:linear-gradient(135deg,#e9edf2 0%,#bfc9d6 55%,#7e8ea5 100%);clip-path:polygon(16% 0,100% 0,100% 100%,0 100%,22% 50%)}
.about-text{position:absolute;left:95px;top:70px;width:420px;color:var(--white)}
.about h2{font-size:32px;margin-bottom:18px}
.about p{font-size:14.5px;line-height:1.75}
.btn-white{display:inline-block;margin-top:20px;background:var(--white);color:var(--navy);font-size:13px;padding:9px 16px}
.services{position:absolute;top:1410px;left:0;width:1200px;text-align:center}
.section-title{font-size:31px;font-weight:700;color:var(--navy-deep)}
.title-rule{width:60px;height:2px;background:var(--navy);margin:12px auto 14px}
.services-lead{font-size:15px;color:#333;line-height:1.5;width:560px;margin:0 auto}
.service-grid{position:absolute;top:154px;left:110px;width:985px;display:grid;grid-template-columns:repeat(4,1fr);gap:28px 16px;text-align:left}
.service-card{height:202px;border:1px solid var(--line);padding:22px 20px;box-shadow:0 1px 3px rgba(0,0,0,.08)}
.service-card h4{font-size:13.5px;font-weight:700;margin:12px 0 6px;color:#111}
.service-card p{font-size:12.5px;line-height:1.35;color:#333;height:52px;overflow:hidden}
.read-more{font-size:12px;color:#444;margin-top:6px}
.testimonials{position:absolute;top:2068px;left:0;width:1200px;height:293px;background:linear-gradient(120deg,#123a7a,#1c4b92 50%,#0f3270)}
.quote{position:absolute;top:60px;width:500px;height:175px;border:1px solid rgba(255,255,255,.6);color:var(--white);padding:18px 20px}
.quote:nth-child(1){left:100px}.quote:nth-child(2){left:610px}
.quote p{font-size:15px;line-height:1.45}
.author{display:flex;align-items:center;gap:14px;margin-top:12px}
.avatar{width:58px;height:58px;background:linear-gradient(#d9c2a8,#a58670);border:2px solid var(--white)}
.author b{display:block;font-size:14px}.author span{font-size:12px}
.contact{position:absolute;top:2436px;left:0;width:1200px;text-align:center}
.contact-form{position:absolute;top:100px;left:134px;width:636px;text-align:left}
.field-row{display:flex;gap:18px}
.field{flex:1;height:32px;border:2px dashed var(--navy);font-size:12px;color:#999;padding:8px}
.textarea{margin-top:10px;height:218px;border:1px solid #ccc;font-size:12px;color:#777;padding:10px}
.btn-submit{display:inline-block;margin-top:18px;background:var(--navy);color:var(--white);font-size:12px;padding:8px 14px}
.contact-card{position:absolute;top:118px;left:798px;width:304px;height:286px;background:var(--navy);border:2px dashed #fff;outline:4px solid var(--navy);text-align:left;color:var(--white);font-size:13px}
.contact-line{display:flex;align-items:center;gap:14px;padding:16px 20px;border-bottom:1px dashed rgba(255,255,255,.5);min-height:52px}
.contact-line:last-child{border:0}
.map{position:absolute;top:2882px;left:0;width:1200px;height:261px;background:linear-gradient(135deg,#8a8f86,#a9a79c 50%,#7d857f)}
.map-zoom{position:absolute;left:6px;top:6px;width:24px;height:48px;background:var(--white);font-size:18px;text-align:center;line-height:24px}
.site-footer{position:absolute;top:3143px;left:0;width:1200px;height:48px;background:var(--navy-deep);color:var(--white);font-size:13px;text-align:center;line-height:48px}
</style>
</head>
<body>
<div class="page">
  <header class="site-header">
    <div class="brand"><span class="brand-mark"></span>Pelvorix</div>
    <nav class="nav"><span>HOME</span><span>ABOUT US</span><span>SERVICE</span><span>CONTACT</span></nav>
  </header>

  <section class="hero" role="img" aria-label="Photo of a multi-storey apartment building under a blue tint">
    <div class="hero-content">
      <h1>Property Condition Reports</h1>
      <p>Before moving ahead on any loan approval, financial institutions need to know the condition of existing structures. Our professional staff will give you the details you need to make sound business decisions.</p>
      <span class="btn-light">LEARN MORE</span>
    </div>
  </section>

  <section class="features">
    <div class="feature"><div class="diamond"><svg width="26" height="22" viewBox="0 0 26 22"><circle cx="9" cy="6" r="4" fill="#fff"/><circle cx="18" cy="6" r="4" fill="#fff"/><path d="M1 21c0-6 4-9 8-9s8 3 8 9zM13 21c0-5 2-9 5-9s7 3 7 9z" fill="#fff"/></svg></div><h3>LOREM IPSUM</h3><p>dolor sit amet, consectetur<br>adipiscing elit. Quisque imperdiet.</p></div>
    <div class="feature"><div class="diamond"><svg width="26" height="22" viewBox="0 0 26 22"><circle cx="9" cy="6" r="4" fill="#fff"/><circle cx="18" cy="6" r="4" fill="#fff"/><path d="M1 21c0-6 4-9 8-9s8 3 8 9zM13 21c0-5 2-9 5-9s7 3 7 9z" fill="#fff"/></svg></div><h3>LOREM IPSUM</h3><p>dolor sit amet, consectetur<br>adipiscing elit. Quisque imperdiet.</p></div>
    <div class="feature"><div class="diamond"><svg width="26" height="22" viewBox="0 0 26 22"><circle cx="9" cy="6" r="4" fill="#fff"/><circle cx="18" cy="6" r="4" fill="#fff"/><path d="M1 21c0-6 4-9 8-9s8 3 8 9zM13 21c0-5 2-9 5-9s7 3 7 9z" fill="#fff"/></svg></div><h3>LOREM IPSUM</h3><p>dolor sit amet, consectetur<br>adipiscing elit. Quisque imperdiet.</p></div>
  </section>

  <section class="about">
    <div class="about-photo" role="img" aria-label="Photo of a business team in a meeting around a table"></div>
    <div class="about-text">
      <h2>About Us</h2>
      <p>Founded in 1990, Pelvorix Consultants prides itself in providing customized, expert services to its clients. Our staff includes professionals who are credentialed and have years of real-world experience. We are committed to providing our clients with expert analysis of proposed and ongoing</p>
      <span class="btn-white">&#9656; More Info</span>
    </div>
  </section>

  <section class="services">
    <h2 class="section-title">Our Services</h2>
    <div class="title-rule"></div>
    <p class="services-lead">Before moving ahead on any loan approval, financial institutions need to know the condition of existing structures.</p>
    <div class="service-grid">
      <div class="service-card"><svg width="26" height="26" viewBox="0 0 26 26"><rect x="2" y="3" width="22" height="15" fill="#0f2f6b"/><rect x="9" y="20" width="8" height="3" fill="#0f2f6b"/></svg><h4>Property Condition Reports</h4><p>Before moving ahead on any loan approval, financial institutions need to know</p><div class="read-more">Read More &#9656;</div></div>
      <div class="service-card"><svg width="26" height="26" viewBox="0 0 26 26"><rect x="2" y="2" width="22" height="22" fill="#0f2f6b"/><circle cx="13" cy="13" r="6" fill="none" stroke="#fff" stroke-width="2"/></svg><h4>Plan &amp; Cost Reviews</h4><p>Our Plan &amp; Cost Reviews provide lending institutions with expert analysis of new</p><div class="read-more">Read More &#9656;</div></div>
      <div class="service-card"><svg width="26" height="26" viewBox="0 0 26 26"><rect x="5" y="11" width="16" height="13" fill="#0f2f6b"/><path d="M8 11V7a5 5 0 0110 0v4" fill="none" stroke="#0f2f6b" stroke-width="2.5"/></svg><h4>Construction Funding Inspections</h4><p>Lending institutions rarely have employees with the expertise needed to</p><div class="read-more">Read More &#9656;</div></div>
      <div class="service-card"><svg width="26" height="26" viewBox="0 0 26 26"><circle cx="13" cy="8" r="6" fill="#0f2f6b"/><path d="M2 25c0-8 5-11 11-11s11 3 11 11z" fill="#0f2f6b"/></svg><h4>Environmental Transaction Screens</h4><p>Environmental Transaction Screens provide an economical but meaningful</p><div class="read-more">Read More &#9656;</div></div>
      <div class="service-card"><svg width="26" height="26" viewBox="0 0 26 26"><path d="M2 5h10v18H2zM14 5h10v18H14z" fill="#0f2f6b"/></svg><h4>Phase I Environmental Site Assessment</h4><p>With reasonable pricing and a quick turnaround, our staff provides</p><div class="read-more">Read More &#9656;</div></div>
      <div class="service-card"><svg width="26" height="26" viewBox="0 0 26 26"><circle cx="6" cy="10" r="3" fill="#0f2f6b"/><circle cx="13" cy="8" r="3" fill="#0f2f6b"/><circle cx="20" cy="10" r="3" fill="#0f2f6b"/><path d="M1 22c0-5 3-8 12-8s12 3 12 8z" fill="#0f2f6b"/></svg><h4>Aenean accumsan</h4><p>Lorem ipsum dolor sit amet, consectetur adipiscing elit. Suspendisse</p><div class="read-more">Read More &#9656;</div></div>
      <div class="service-card"><svg width="26" height="26" viewBox="0 0 26 26"><rect x="3" y="14" width="4" height="10" fill="#0f2f6b"/><rect x="9" y="9" width="4" height="15" fill="#0f2f6b"/><rect x="15" y="12" width="4" height="12" fill="#0f2f6b"/><rect x="21" y="5" width="4" height="19" fill="#0f2f6b"/></svg><h4>Aenean accumsan</h4><p>Lorem ipsum dolor sit amet, consectetur adipiscing elit. Suspendisse</p><div class="read-more">Read More &#9656;</div></div>
      <div class="service-card"><svg width="26" height="26" viewBox="0 0 26 26"><circle cx="13" cy="11" r="9" fill="none" stroke="#0f2f6b" stroke-width="2.5"/><circle cx="13" cy="11" r="3" fill="#0f2f6b"/><rect x="6" y="21" width="14" height="3" fill="#0f2f6b"/></svg><h4>Aenean accumsan</h4><p>Lorem ipsum dolor sit amet, consectetur adipiscing elit. Suspendisse</p><div class="read-more">Read More &#9656;</div></div>
    </div>
  </section>

  <section class="testimonials" role="img" aria-label="Blue tinted photo of a workspace behind client quotes">
    <div class="quote"><p>&ldquo;Consectetur adipiscing elit. Maiores a molestias, exercitationem at? Neque eaque modi minus consequuntur sapiente quasi amet? Animi.&rdquo;</p><div class="author"><div class="avatar" role="img" aria-label="Client portrait"></div><div><b>Marten Holl</b><span>Designer</span></div></div></div>
    <div class="quote"><p>&ldquo;Consectetur adipiscing elit. Maiores a molestias, exercitationem at? Neque eaque modi minus consequuntur sapiente quasi amet? Animi.&rdquo;</p><div class="author"><div class="avatar" role="img" aria-label="Client portrait"></div><div><b>Marten Holl</b><span>Designer</span></div></div></div>
  </section>

  <section class="contact">
    <h2 class="section-title">Contact Us</h2>
    <div class="title-rule"></div>
    <div class="contact-form">
      <div class="field-row"><div class="field">Your name</div><div class="field">Your email</div><div class="field">Phone</div><div class="field">Subject</div></div>
      <div class="textarea">Your message</div>
      <span class="btn-submit">SUBMIT</span>
    </div>
    <div class="contact-card">
      <div class="contact-line"><svg width="14" height="10" viewBox="0 0 14 10"><rect width="14" height="10" fill="#fff"/><path d="M0 0l7 6 7-6" stroke="#0f2f6b" fill="none"/></svg>info@pelvorix.com</div>
      <div class="contact-line"><svg width="12" height="14" viewBox="0 0 12 14"><path d="M2 0h3l1 4-2 1c1 2 2 4 4 5l1-2 3 1v3c-6 1-12-6-10-12z" fill="#fff"/></svg>555-014-2287</div>
      <div class="contact-line"><svg width="12" height="16" viewBox="0 0 12 16"><path d="M6 0a6 6 0 016 6c0 4-6 10-6 10S0 10 0 6a6 6 0 016-6z" fill="#fff"/><circle cx="6" cy="6" r="2" fill="#0f2f6b"/></svg><span>148 Linden Ave Suite 12,<br>Marrow Township, NJ 07460</span></div>
      <div class="contact-line"><svg width="14" height="12" viewBox="0 0 14 12"><path d="M0 0h14v9H5l-4 3V9H0z" fill="#fff"/></svg>Left Some Word</div>
    </div>
  </section>

  <div class="map" role="img" aria-label="Street map showing the office location"><div class="map-zoom">+<br>&minus;</div></div>

  <footer class="site-footer">Copyright 2014 | pelvorix.com | 148 Linden Ave #12 Marrow Township, NJ 07460 | 555-014-2287</footer>
</div>
</body>
</html>
```